I need a business card/logo designed that obviously describes my business. We are a residential appraisal and home inspection company in Springfield, MO. We offer residential appraisals, home inspection, pest inspection and radon gas measurement. We have been in business for 18 years and hold state certified residential appraisal licenses and DRUMI certified home inspection licenses. I have a logo that I really like and will attach, but would be open to new suggestions. I like more modern designs than traditional and would like a two sided card with our services, licenses and qualifications on the back.

```html
<!DOCTYPE html>
<html lang="en">
<head>
<meta charset="utf-8">
<title>Larkvale Dwelling Review – Business Card</title>
<link href="https://fonts.googleapis.com/css2?family=Arimo:wght@400;700&display=swap" rel="stylesheet">
<style>
  :root {
    --backdrop: #e9e4dc;
    --card-white: #fbfbfa;
    --tan: #a89470;
    --tan-light: #c2ae86;
    --tan-dark: #8d7a58;
    --gold: #e8a521;
    --gold-soft: #f0b73a;
    --text-gold: #d69b2a;
    --white: #ffffff;
  }
  * { margin: 0; padding: 0; box-sizing: border-box; }
  html, body { width: 1200px; height: 892px; overflow: hidden; }
  body {
    background: var(--backdrop);
    font-family: "Arimo", Arial, sans-serif;
    position: relative;
  }
  .card {
    position: absolute;
    left: 250px;
    width: 700px;
    height: 400px;
    overflow: hidden;
    box-shadow: 0 6px 18px rgba(60, 45, 20, 0.25);
  }
  .card-front { top: 30px; background: var(--card-white); }
  .card-back {
    top: 462px;
    background: linear-gradient(135deg, var(--tan-light) 0%, var(--tan) 55%, var(--tan-dark) 100%);
  }

  /* front */
  .front-band {
    position: absolute; left: 0; right: 0; bottom: 0; height: 62px;
    background: var(--tan);
    border-top: 6px solid var(--gold);
  }
  .divider-vertical {
    position: absolute; left: 330px; top: 40px; width: 2px; height: 250px;
    background: var(--gold);
  }
  .brand-front {
    position: absolute; left: 36px; top: 150px; width: 270px;
    color: var(--tan);
    font-weight: 700; font-size: 30px; line-height: 1.15;
    display: flex; align-items: center; gap: 14px;
  }
  .brand-mark {
    flex: none; width: 16px; height: 16px; background: var(--gold);
  }
  .contact-list {
    position: absolute; left: 360px; top: 62px;
    list-style: none;
    color: var(--text-gold); font-size: 17px; line-height: 30px;
  }
  .contact-list li { display: flex; align-items: center; gap: 12px; }
  .contact-list .address { align-items: flex-start; }
  .contact-icon {
    flex: none; width: 18px; height: 18px; background: var(--gold);
    border-radius: 2px; display: flex; align-items: center; justify-content: center;
  }
  .address .contact-icon { margin-top: 6px; }
  .contact-icon svg { width: 12px; height: 12px; }

  /* back */
  .services {
    position: absolute; left: 50px; top: 30px; right: 50px;
    list-style: none;
    display: grid;
    grid-template-columns: 1fr 1fr;
    grid-template-rows: repeat(5, 30px);
    grid-auto-flow: column;
    column-gap: 40px;
    color: var(--white); font-size: 17px; line-height: 30px;
  }
  .services li { display: flex; align-items: center; gap: 12px; white-space: nowrap; }
  .bullet {
    flex: none; width: 10px; height: 10px; border-radius: 50%;
    border: 2px solid var(--white);
  }
  .divider-back {
    position: absolute; left: 50px; right: 50px; top: 200px; height: 2px;
    background: var(--white); opacity: 0.85;
  }
  .brand-back {
    position: absolute; left: 0; right: 0; top: 236px;
    color: var(--white); font-weight: 700; font-size: 34px;
    display: flex; align-items: center; justify-content: center; gap: 16px;
  }
  .brand-back .brand-mark { background: var(--white); }
  .back-band {
    position: absolute; left: 0; right: 0; bottom: 0; height: 48px;
    background: linear-gradient(90deg, var(--gold) 0%, var(--gold-soft) 100%);
    border-top: 6px solid var(--white);
  }
</style>
</head>
<body>

<section class="card card-front" aria-label="Card front">
  <div class="brand-front">
    <span class="brand-mark"></span>
    <span class="brand-name">Larkvale Dwelling Review</span>
  </div>
  <div class="divider-vertical"></div>
  <ul class="contact-list">
    <li><span class="contact-icon"><svg viewBox="0 0 12 12"><path d="M2 1h3l1 3-2 1a6 6 0 0 0 3 3l1-2 3 1v3c-6 0-9-3-9-9z" fill="#fff"/></svg></span>555-014-3414</li>
    <li><span class="contact-icon"><svg viewBox="0 0 12 12"><rect x="3" y="1" width="6" height="10" rx="1" fill="#fff"/></svg></span>555-014-9089</li>
    <li><span class="contact-icon"><svg viewBox="0 0 12 12"><rect x="1" y="4" width="10" height="6" fill="#fff"/><rect x="3" y="1" width="6" height="3" fill="#fff"/></svg></span>555-014-8936</li>
    <li><span class="contact-icon"><svg viewBox="0 0 12 12"><rect x="1" y="2.5" width="10" height="7" fill="#fff"/><path d="M1 3l5 4 5-4" stroke="#e8a521" fill="none"/></svg></span>info@larkvalereview.com</li>
    <li class="address"><span class="contact-icon"><svg viewBox="0 0 12 12"><path d="M6 11S2 7 2 4.5a4 4 0 0 1 8 0C10 7 6 11 6 11z" fill="#fff"/></svg></span><span>Larkvale Dwelling Review<br>4820 W Alder Lane; Suite B<br>Springfield, MO 65899</span></li>
  </ul>
  <div class="front-band"></div>
</section>

<section class="card card-back" aria-label="Card back">
  <ul class="services">
    <li><span class="bullet"></span>Home inspection</li>
    <li><span class="bullet"></span>Property inspection</li>
    <li><span class="bullet"></span>Residential appraisal</li>
    <li><span class="bullet"></span>Termite inspection</li>
    <li><span class="bullet"></span>Radon measurement</li>
    <li><span class="bullet"></span>Mold inspection</li>
    <li><span class="bullet"></span>Home staging</li>
    <li><span class="bullet"></span>DRUMI certification</li>
    <li><span class="bullet"></span>State certified appraisal</li>
  </ul>
  <div class="divider-back"></div>
  <div class="brand-back">
    <span class="brand-mark"></span>
    <span class="brand-name">Larkvale Dwelling Review</span>
  </div>
  <div class="back-band"></div>
</section>

</body>
</html>
```